Southport Billboard for Hiring more CDL drivers

I need a catch design for a bill board (size 10ft by 36 ft) to catch the attention for semi truck drivers.
In the design I want it to include:
-My company logo along with my website(brisklanefreighters.com) and my number(503-217-6095) for contact info.
-I also need it to say earn up to $90,000 a year
-I will send a few photos to choose from
-I need the logo to look clean and simple! I don't want it to be cluttered just clean, simple and catchy.!

Target Market(s)

CDL Class A holders
Semi Truck Drivers

Industry/Entity Type

Trucking Company

Font styles to use
Other font styles liked:
• a font to match my logo

Requirements
Must have
• "Make up to $90,000"
"brisklanefreighters.com"
"503-217-6095"

```html
<!DOCTYPE html>
<html lang="en">
<head>
<meta charset="utf-8">
<title>Brisk Lane Freighters – Hiring CDL Drivers Billboard</title>
<link rel="stylesheet" href="https://fonts.googleapis.com/css2?family=Oswald:ital,wght@0,500;0,600;0,700&display=swap">
<style>
  :root {
    --page: #ecebe8;
    --panel-black: #111111;
    --panel-dark: #252525;
    --brand-red: #e8101a;
    --brand-yellow: #ffd600;
    --white: #ffffff;
    --ink: #0c0c0c;
  }
  * { margin: 0; padding: 0; box-sizing: border-box; }
  html, body {
    width: 1188px; height: 1200px; overflow: hidden;
    background: var(--page);
    font-family: "Oswald", "Arial Narrow", sans-serif;
  }
  .billboard {
    position: absolute; left: 0; top: 435px;
    width: 1188px; height: 330px; overflow: hidden;
    background: radial-gradient(ellipse at 40% 40%, var(--panel-dark), var(--panel-black) 75%);
  }
  .billboard-shapes { position: absolute; inset: 0; }
  .brand-name {
    position: absolute; left: 76px; top: 22px;
    color: var(--white); font-weight: 700;
    font-size: 42px; line-height: 1; letter-spacing: 1px;
    text-transform: uppercase;
  }
  .brand-name .brand-sub {
    display: block; font-size: 16px; letter-spacing: 9px; margin-top: 6px;
    padding-left: 178px;
  }
  .pay-lead {
    position: absolute; left: 90px; top: 100px;
    color: var(--white); font-weight: 600; font-size: 28px; line-height: 1;
  }
  .pay-amount {
    position: absolute; left: 84px; top: 134px;
    color: var(--brand-red); font-weight: 700; font-size: 66px; line-height: 1;
    letter-spacing: -1px; transform: skewX(-6deg);
  }
  .pay-period {
    position: absolute; left: 326px; top: 152px;
    color: var(--white); font-weight: 600; font-size: 32px; line-height: 1;
  }
  .phone-line {
    position: absolute; left: 122px; top: 224px;
    color: var(--ink); font-weight: 600; font-size: 22px; line-height: 30px;
  }
  .hiring-line {
    position: absolute; left: 86px; top: 283px;
    color: var(--white); font-weight: 600; font-size: 32px; line-height: 40px;
  }
  .hiring-line .accent { color: var(--brand-yellow); }
  .web-address {
    position: absolute; left: 740px; top: 286px;
    color: var(--ink); font-weight: 600; font-size: 25px; line-height: 36px;
  }
</style>
</head>
<body>
<main class="billboard">
  <svg class="billboard-shapes" width="1188" height="330" viewBox="0 0 1188 330" aria-hidden="false">
    <defs>
      <linearGradient id="truck-photo-tone" x1="0" y1="0" x2="1" y2="1">
        <stop offset="0" stop-color="#b5c2cc"/>
        <stop offset="0.35" stop-color="#c8141c"/>
        <stop offset="0.7" stop-color="#8f1016"/>
        <stop offset="1" stop-color="#5e5e60"/>
      </linearGradient>
      <linearGradient id="fleet-photo-tone" x1="0" y1="0" x2="1" y2="0">
        <stop offset="0" stop-color="#3d8a9a"/>
        <stop offset="0.6" stop-color="#b02a2e"/>
        <stop offset="1" stop-color="#c9cdd2"/>
      </linearGradient>
      <linearGradient id="yard-photo-tone" x1="0" y1="0" x2="0" y2="1">
        <stop offset="0" stop-color="#6f9fe0"/>
        <stop offset="0.45" stop-color="#c3161c"/>
        <stop offset="1" stop-color="#7a7873"/>
      </linearGradient>
    </defs>

    <polygon class="photo-main-truck" role="img" aria-label="Photo of a red semi truck with flatbed trailer"
      points="520,40 788,0 1112,330 470,330 530,220" fill="url(#truck-photo-tone)"/>
    <polygon class="photo-fleet" role="img" aria-label="Photo of a blue and a red semi truck parked side by side"
      points="795,0 1100,0 940,148" fill="url(#fleet-photo-tone)"/>
    <polygon class="photo-yard-truck" role="img" aria-label="Photo of a red semi truck in a parking lot"
      points="1117,0 1188,0 1188,330 1128,330 954,158" fill="url(#yard-photo-tone)"/>

    <polygon class="divider-stripe" points="783,0 796,0 1124,330 1108,330" fill="var(--panel-black)"/>
    <polygon class="divider-stripe" points="1100,0 1117,0 954,158 944,146" fill="var(--panel-black)"/>

    <polygon class="hiring-band" points="0,279 472,279 432,330 0,330" fill="var(--brand-red)"/>
    <polygon class="web-band" points="728,282 1064,282 1112,330 706,330" fill="var(--brand-yellow)"/>

    <polygon class="phone-band" points="110,222 403,222 388,258 94,258" fill="var(--brand-yellow)"/>
    <polygon class="phone-icon-band" points="86,222 120,222 104,258 70,258" fill="var(--brand-red)"/>
    <path class="phone-icon" fill="var(--white)"
      d="M88 232 c2-1 4 0 5 2 l2 3 c1 1 0 3-1 4 l-1 1 c1 2 3 4 5 5 l1-1 c1-1 3-2 4-1 l3 2 c2 1 2 3 1 5 l-1 1 c-2 2-6 2-10-1 c-4-3-7-7-8-11 c-1-3 0-6 1-7 z"/>
  </svg>

  <div class="brand-name">Brisk Lane<span class="brand-sub">Freighters</span></div>
  <p class="pay-lead">Earn up to</p>
  <p class="pay-amount">$90,000</p>
  <p class="pay-period">a year</p>
  <p class="phone-line">Call Us Today: 503-217-6095</p>
  <p class="hiring-line">Hiring <span class="accent">CDL</span> drivers</p>
  <p class="web-address">www.brisklanefreighters.com</p>
</main>
</body>
</html>
```